Kelvo Auto - help to get me noticed

We not long ago tasked Pixel Harbour to design a logo for my business. I'm happy with the result so would like to have a business card designed as a follow up.

It's an Automotive service and repair business that offers the following -
- Servicing
- General repairs
- Brakes
- Detailing
- Integrity

Kelvo Automotive
Dallin Mereth
0471 926 317

Target Market(s)

Everyday people with the ability to reach out to corporate customers also.

Industry/Entity Type

Automotive

Contact Information for Business Card

Black card, logo, name and phone number on front. Other details on back of card.

```html
<!DOCTYPE html>
<html lang="en">
<head>
<meta charset="utf-8">
<title>Kelvo Automotive – Business Card</title>
<link rel="stylesheet" href="https://fonts.googleapis.com/css2?family=Arimo:wght@400;700&display=swap">
<style>
  :root {
    --stage: #2b2b2b;
    --card-dark: #1b1b1b;
    --lime: #a6cf21;
    --lime-light: #b4d624;
    --green-deep: #5aa623;
    --white: #ffffff;
    --text-soft: #e6e6e6;
  }
  * { box-sizing: border-box; margin: 0; padding: 0; }
  html, body {
    width: 1200px; height: 1015px; overflow: hidden;
    background: var(--stage);
    font-family: "Arimo", Arial, sans-serif;
  }
  .stage {
    position: relative; width: 1200px; height: 1015px;
  }
  .card {
    position: absolute; left: 280px; width: 640px; height: 366px;
    box-shadow: 0 10px 28px rgba(0,0,0,.55);
    overflow: hidden;
  }
  .card--front { top: 90px; }
  .card--back { top: 550px; background: var(--card-dark); }

  .front-pattern {
    position: absolute; inset: 0;
    background: linear-gradient(155deg, var(--lime-light) 0%, var(--lime) 45%, var(--green-deep) 100%);
  }
  .front-name {
    position: absolute; right: 96px; top: 178px;
    color: var(--white); font-weight: 700; font-size: 40px; letter-spacing: 1px;
  }

  .holder-name {
    position: absolute; right: 56px; top: 52px;
    color: var(--lime); font-weight: 400; font-size: 26px; letter-spacing: .5px;
  }
  .brand {
    position: absolute; left: 60px; top: 118px;
    color: var(--lime); font-weight: 700; line-height: 1;
  }
  .brand__main { display: block; font-size: 64px; letter-spacing: 1px; }
  .brand__sub { display: block; font-size: 30px; letter-spacing: 6px; margin-top: 6px; }
  .divider {
    position: absolute; left: 60px; right: 40px; top: 238px;
    height: 1px; background: var(--lime);
  }
  .contacts {
    position: absolute; left: 70px; top: 262px; list-style: none;
    color: var(--text-soft); font-size: 17px; line-height: 27px;
  }
  .contacts li { display: flex; align-items: center; gap: 10px; }
  .contacts svg { width: 16px; height: 16px; flex: none; }
  .services {
    position: absolute; right: 40px; top: 262px;
    color: var(--text-soft); font-size: 17px; line-height: 27px; text-align: left;
  }
  .services .sep { color: var(--lime); padding: 0 4px; }
</style>
</head>
<body>
<main class="stage">
  <section class="card card--front">
    <div class="front-pattern" role="img" aria-label="Lime-to-green gradient background with a faint repeating brand pattern"></div>
    <div class="front-name">Kelvo</div>
  </section>

  <section class="card card--back">
    <div class="holder-name">DALLIN MERETH</div>
    <div class="brand">
      <span class="brand__main">KELVO</span>
      <span class="brand__sub">AUTOMOTIVE</span>
    </div>
    <div class="divider"></div>
    <ul class="contacts">
      <li>
        <svg viewBox="0 0 16 16" aria-hidden="true"><path fill="#a6cf21" d="M3.5 1.5l2.5 2.5-1.4 1.8a8 8 0 0 0 5.6 5.6l1.8-1.4 2.5 2.5-1.8 2A11 11 0 0 1 1.5 3.3z"/></svg>
        0471 926 317
      </li>
      <li>
        <svg viewBox="0 0 16 16" aria-hidden="true"><rect x="1" y="3" width="14" height="10" fill="#a6cf21"/><path d="M1 3l7 6 7-6" fill="none" stroke="#1b1b1b" stroke-width="1.4"/></svg>
        info@kelvoautomotive.com
      </li>
      <li>
        <svg viewBox="0 0 16 16" aria-hidden="true"><g fill="none" stroke="#a6cf21" stroke-width="1.4"><circle cx="8" cy="8" r="6.5"/><ellipse cx="8" cy="8" rx="2.8" ry="6.5"/><path d="M1.5 8h13M2.5 4.8h11M2.5 11.2h11"/></g></svg>
        www.kelvoautomotive.com
      </li>
    </ul>
    <div class="services">
      <div>Servicing<span class="sep">|</span>General repairs</div>
      <div>Brakes<span class="sep">|</span>Detailing<span class="sep">|</span>Integrity</div>
    </div>
  </section>
</main>
</body>
</html>
```